Business Card Design Project

Looking for a logo and business card for a Real State Business i will be opening. The name is not choosen yet , but will probably be RTV IMOVEIS.
I was thinking black and silver colors, but am open to nice ideas.
I did add a business card that i liked a lot, am looking for something like that, with logo in black or silver in a black card. The logo i was thinking in the letters RTV as i uploaded or something or little and cute buildings or a house...just ideas, can be any nice logo.
Updates

You guys can add other colors if you want, I like colors very "BRIGHT" and "open", like red, pink, strong colors. almost glow in the dark colors. lol

Designers,

I've increased more 88 dollars in the budget for 1st place cause I will want envelope designs... small and big sizes.

So 1st place is now U$248,00. 

No need to send the envelope designs right now... only the business cards designs.

Thank you.

Industry/Entity Type

Business

Requirements
Must have
• Renata Tavares Vilela

www.RTVimoveis-exemplo.com.br

+554188316402

renata@rtvimoveis-exemplo.com.br

```html
<!DOCTYPE html>
<html lang="pt-BR">
<head>
<meta charset="utf-8">
<title>RTV IMOVEIS – Cartão de visita</title>
<link href="https://fonts.googleapis.com/css2?family=Ubuntu:wght@400;500;700&display=swap" rel="stylesheet">
<style>
  :root {
    --backdrop: #3a3a3a;
    --card: #2b2c2c;
    --silver: #8e8e8e;
    --white: #ffffff;
    --text-light: #f2f2f2;
    --sky-dark: #0e0e0e;
    --sky-mid: #1c1c1c;
    --sky-light: #a0a0a0;
  }
  html, body {
    margin: 0;
    width: 1200px;
    height: 900px;
    overflow: hidden;
    background: var(--backdrop);
    font-family: "Ubuntu", sans-serif;
  }
  .canvas { position: relative; width: 1200px; height: 900px; }
  .card {
    position: absolute;
    background: var(--card);
    overflow: hidden;
    box-shadow: 0 2px 8px rgba(0,0,0,0.45);
  }
  .card-front { left: 187px; top: 192px; width: 285px; height: 514px; }
  .card-back { left: 500px; top: 308px; width: 514px; height: 283px; }

  .brand-initials, .brand-word {
    position: absolute;
    margin: 0;
    font-weight: 700;
    line-height: 1;
    white-space: nowrap;
  }
  .card-front .brand-initials,
  .card-front .brand-word {
    left: 0; right: 0;
    text-align: center;
    color: var(--silver);
  }
  .card-front .brand-initials { top: 150px; font-size: 118px; letter-spacing: -2px; }
  .card-front .brand-word { top: 393px; font-size: 40px; letter-spacing: 0.5px; }

  .skyline {
    position: absolute;
    left: 0; right: 0; bottom: 0;
    height: 125px;
    background:
      linear-gradient(to bottom, var(--card) 0%, rgba(43,44,44,0) 45%),
      linear-gradient(155deg, var(--sky-dark) 0%, var(--sky-mid) 52%, var(--sky-light) 100%);
  }
  .card-back .brand-initials,
  .card-back .brand-word { color: var(--white); }
  .card-back .brand-initials { left: 40px; top: 70px; font-size: 66px; letter-spacing: -1px; }
  .card-back .brand-word { left: 42px; top: 218px; font-size: 23px; }

  .contact { position: absolute; left: 262px; top: 48px; color: var(--text-light); }
  .contact-name { margin: 0 0 24px; font-size: 20px; font-weight: 400; }
  .contact-line { margin: 0; font-size: 13px; line-height: 17px; }
  .contact-phone { margin-bottom: 16px; }
</style>
</head>
<body>
<main class="canvas">
  <section class="card card-front" aria-label="Frente do cartão">
    <p class="brand-initials">RTV</p>
    <p class="brand-word">IMOVEIS</p>
  </section>

  <section class="card card-back" aria-label="Verso do cartão">
    <div class="skyline" role="img" aria-label="Silhueta de prédios da cidade em degradê preto para prata"></div>
    <p class="brand-initials">RTV</p>
    <p class="brand-word">IMOVEIS</p>
    <div class="contact">
      <h1 class="contact-name">Renata Tavares Vilela</h1>
      <p class="contact-line contact-phone">+554 188 316 402</p>
      <p class="contact-line">renata@rtvimoveis-exemplo.com.br</p>
      <p class="contact-line">www.RTVimoveis-exemplo.com.br</p>
    </div>
  </section>
</main>
</body>
</html>
```